Fernbrook Yield - Online-only garden installation company

Online-only garden installation company. Our demographic is middle aged / suburban women, and we anticipate Facebook driving traffic to this website, as well as referrals from garden centers. The website must be very simple in design and function.

All orders will be placed through the website, including size of garden (3 options), location in yard, payment, and scheduling of installation date.

The website should employ a 3 step process:

Step 1: Select garden size. Either an 4' X 4', 8' X 4', or 12' X 4'.

Step 2: Select a location. We would like to use google maps to look up a US address, then "drag and drop" one of the garden sizes from step 1 to the location the customer would like us to install the garden at their home.

Step 3: Pick an installation date and pay. Using an online calendar the customer will pick a date, and then pay for the installation via credit card.

The website will be linked to an email account, FernbrookYield@mailvista.example to inform us of orders placed.

Target Market(s)

Our demographic is middle aged / suburban women, and we anticipate Facebook driving traffic to this website, as well as referrals from garden centers.

Industry/Entity Type

It Company

Coding

Coded - Design and coding required

Number of Pages Required

4 page

Requirements
Must have
• Scheduling and payment options.

```html
<!DOCTYPE html>
<html lang="en">
<head>
<meta charset="utf-8">
<title>Fernbrook Yield — Garden Installation</title>
<link href="https://fonts.googleapis.com/css2?family=Roboto+Slab:wght@400;700&family=Open+Sans:wght@400;600;700&display=swap" rel="stylesheet">
<style>
:root{
  --green:#2f7a3c;
  --green-dark:#255f2f;
  --orange:#e0592a;
  --ink:#333333;
  --muted:#777777;
  --light:#f4f4f4;
  --footer:#3b3b3b;
  --footer-deep:#2e2e2e;
  --white:#ffffff;
}
*{box-sizing:border-box;margin:0;padding:0}
html,body{width:1200px;height:3400px;overflow:hidden;background:var(--white)}
body{font-family:"Open Sans",Arial,sans-serif;color:var(--ink);position:relative}

/* header */
.topbar{position:absolute;top:0;left:0;width:1200px;height:64px;background:var(--white);z-index:3;box-shadow:0 2px 6px rgba(0,0,0,.12)}
.searchbox{position:absolute;left:30px;top:17px;width:160px;height:30px;border:1px solid #ccc;font-size:12px;color:var(--muted);display:flex;align-items:center;justify-content:space-between;padding:0 10px}
.nav{position:absolute;top:0;height:64px;display:flex;align-items:center;gap:16px;font-size:12px;font-weight:600;text-transform:uppercase;color:var(--ink);white-space:nowrap}
.nav-left{right:700px}
.nav-right{left:690px}
.actions{position:absolute;right:30px;top:17px;display:flex;gap:6px}
.pill{height:30px;padding:0 9px;font-size:10.5px;font-weight:700;color:var(--white);display:flex;align-items:center;text-transform:uppercase;white-space:nowrap}
.pill.green{background:var(--green)}
.pill.orange{background:var(--orange)}
.brand-badge{position:absolute;left:530px;top:0;width:140px;height:132px;background:var(--white);z-index:4;display:flex;flex-direction:column;align-items:center;justify-content:center;gap:8px;box-shadow:0 3px 8px rgba(0,0,0,.15)}
.brand-badge .dot{width:34px;height:34px;border-radius:50%;background:var(--green)}
.brand-name{font-family:"Roboto Slab",Georgia,serif;font-weight:700;font-size:14px;line-height:1.25;color:var(--green);text-transform:uppercase;letter-spacing:1px;text-align:center}

/* hero */
.hero{position:absolute;top:0;left:0;width:1200px;height:760px;background:linear-gradient(120deg,#5d7a3a 0%,#8aa556 35%,#4f6b2e 65%,#2f4a22 100%)}
.order-strip{position:absolute;left:0;top:620px;width:1200px;height:140px;background:rgba(35,80,40,.88);text-align:center;color:var(--white)}
.order-strip h2{font-family:"Roboto Slab",Georgia,serif;font-weight:400;font-size:26px;text-transform:uppercase;margin-top:22px;letter-spacing:1px}
.order-form{display:flex;justify-content:center;gap:12px;margin-top:20px}
.field{width:250px;height:40px;background:var(--white);color:var(--muted);font-size:13px;display:flex;align-items:center;justify-content:space-between;padding:0 12px}
.btn{background:var(--orange);color:var(--white);font-weight:700;font-size:13px;text-transform:uppercase;display:inline-flex;align-items:center;justify-content:center}
.order-form .btn{width:130px;height:40px}

/* section heads */
.section-title{font-family:"Roboto Slab",Georgia,serif;font-weight:400;font-size:30px;text-transform:uppercase;text-align:center;color:var(--ink)}
.rule{width:60px;height:3px;background:var(--orange);margin:14px auto 0}
.more{color:var(--orange);font-size:13px;font-weight:700;text-transform:uppercase}

/* welcome */
.welcome{position:absolute;top:800px;left:0;width:1200px;text-align:center}
.welcome p{width:860px;margin:26px auto 22px;font-size:15px;line-height:1.75;color:var(--muted)}

/* services */
.services{position:absolute;top:1100px;left:0;width:1200px;height:460px}
.services-bar{position:absolute;left:0;top:60px;width:440px;height:64px;background:var(--orange);color:var(--white);font-family:"Roboto Slab",Georgia,serif;font-weight:400;font-size:24px;text-transform:uppercase;display:flex;align-items:center;padding-left:70px;white-space:nowrap}
.services-text{position:absolute;left:70px;top:150px;width:330px}
.services-text p{font-size:14px;line-height:1.75;color:var(--muted);margin-bottom:22px}
.services-photo{position:absolute;left:440px;top:20px;width:680px;height:420px;background:linear-gradient(135deg,#e8b93a 0%,#c8764a 30%,#6a5a3e 60%,#3f3a2c 100%)}

/* projects */
.projects{position:absolute;top:1600px;left:0;width:1200px;text-align:center}
.grid{display:grid;grid-template-columns:repeat(3,330px);gap:28px;justify-content:center;margin-top:40px}
.tile{height:236px}
.t1{background:linear-gradient(135deg,#6f9a45,#3e6a2c)}
.t2{background:linear-gradient(135deg,#8c7457,#5e8a3a)}
.t3{background:linear-gradient(135deg,#a8925e,#6e8b4a)}
.t4{background:linear-gradient(135deg,#7f8a60,#4e6a36)}
.t5{background:linear-gradient(135deg,#c9a98c,#4c6f32)}
.t6{background:linear-gradient(135deg,#9a7a50,#5b8b3c)}
.projects .more{display:block;margin-top:32px}

/* testimonial */
.testimonial{position:absolute;top:2350px;left:0;width:1200px;height:410px;background:var(--green);color:var(--white);text-align:center}
.quote-mark{width:64px;height:64px;border:2px solid var(--white);border-radius:50%;margin:50px auto 0;display:flex;align-items:center;justify-content:center;font-family:"Roboto Slab",Georgia,serif;font-size:40px;line-height:1;padding-top:12px}
.testimonial blockquote{width:760px;margin:30px auto 0;font-size:18px;line-height:1.6}
.testimonial .rule{background:var(--white);width:40px;margin-top:26px}
.who{margin-top:18px;font-weight:700;font-size:15px}
.where{font-size:12px;opacity:.85;margin-top:2px}
.arrows{display:flex;justify-content:center;gap:10px;margin-top:18px}

/* call to action */
.cta{position:absolute;top:2760px;left:0;width:1200px;height:260px;background:linear-gradient(90deg,#4a4238 0%,#5c5a45 45%,#3c3a33 100%);text-align:center;color:var(--white)}
.cta::before{content:"";position:absolute;inset:0;background:rgba(0,0,0,.35)}
.cta-inner{position:relative}
.cta h2{font-family:"Roboto Slab",Georgia,serif;font-weight:400;font-size:30px;text-transform:uppercase;padding-top:70px}
.cta .btn{width:200px;height:46px;margin-top:26px}

/* footer */
.footer{position:absolute;top:3020px;left:0;width:1200px;height:380px;background:var(--footer);color:#cfcfcf}
.footer-brand{position:absolute;left:80px;top:70px;display:flex;flex-direction:column;align-items:center;gap:10px}
.footer-brand .dot{width:30px;height:30px;border-radius:50%;background:#cfcfcf}
.footer-brand .brand-name{color:#e6e6e6;font-size:16px}
.col{position:absolute;top:56px}
.col h4{font-size:14px;font-weight:700;color:var(--white);margin-bottom:14px}
.col li{list-style:none;font-size:12px;line-height:1.9}
.c1{left:340px}.c2{left:520px}.c3{left:720px}.c4{left:940px}
.cards{display:grid;grid-template-columns:repeat(3,44px);gap:8px}
.card{height:28px;background:#e8e8e8;border-radius:3px}
.socials{display:flex;gap:6px}
.social{width:30px;height:30px;background:#5a5a5a}
.copyright{position:absolute;left:0;bottom:0;width:1200px;height:56px;background:var(--footer-deep);font-size:12px;display:flex;align-items:center;padding-left:80px}
</style>
</head>
<body>

<section class="hero" role="img" aria-label="Photograph of a smiling woman tending plants in a lush vegetable garden"></section>

<header class="topbar">
  <div class="searchbox">Search
    <svg width="14" height="14" viewBox="0 0 14 14"><circle cx="6" cy="6" r="4.5" fill="none" stroke="#555" stroke-width="1.6"/><line x1="9.3" y1="9.3" x2="13" y2="13" stroke="#555" stroke-width="1.6"/></svg>
  </div>
  <nav class="nav nav-left"><span>Home</span><span>About us</span><span>Services</span></nav>
  <nav class="nav nav-right"><span>Projects</span><span>Shop</span><span>Contact us</span></nav>
  <div class="actions"><span class="pill green">Order now</span><span class="pill green">My account</span><span class="pill orange">0 / Items</span></div>
</header>
<div class="brand-badge"><span class="dot"></span><span class="brand-name">Fernbrook<br>Yield</span></div>

<div class="order-strip">
  <h2>Order now garden installation today!</h2>
  <div class="order-form">
    <div class="field">Select garden size <span>▾</span></div>
    <div class="field">Choose a location
      <svg width="12" height="16" viewBox="0 0 12 16"><path d="M6 1a5 5 0 0 0-5 5c0 4 5 9 5 9s5-5 5-9a5 5 0 0 0-5-5z" fill="#999"/><circle cx="6" cy="6" r="2" fill="#fff"/></svg>
    </div>
    <div class="field">Pick an installation date
      <svg width="14" height="14" viewBox="0 0 14 14"><rect x="1" y="2.5" width="12" height="10.5" fill="none" stroke="#999" stroke-width="1.4"/><line x1="1" y1="5.5" x2="13" y2="5.5" stroke="#999" stroke-width="1.4"/></svg>
    </div>
    <span class="btn">Search</span>
  </div>
</div>

<section class="welcome">
  <h2 class="section-title">Welcome to Fernbrook Yield</h2>
  <div class="rule"></div>
  <p>Lorem ipsum dolor sit amet, consectetur adipiscing elit, sed do eiusmod tempor incididunt ut labore et dolore magna aliqua. Ut enim ad minim veniam, quis nostrud exercitation ullamco laboris nisi ut aliquip ex ea commodo consequat. Duis aute irure dolor in reprehenderit in voluptate velit esse cillum dolore eu fugiat nulla pariatur. Excepteur sint occaecat cupidatat non proident, sunt in culpa qui officia deserunt mollit anim id est laborum.</p>
  <span class="more">Learn more ›</span>
</section>

<section class="services">
  <h2 class="services-bar">Our awesome services</h2>
  <div class="services-text">
    <p>Lorem ipsum dolor sit amet, consectetur adipiscing elit, sed do eiusmod tempor incididunt ut labore et dolore magna aliqua. Ut enim ad minim veniam, quis nostrud exercitation ullamco laboris nisi ut aliquip ex ea commodo consequat. Duis aute irure dolor in reprehenderit in voluptate velit esse cillum dolore eu fugiat nulla pariatur.</p>
    <span class="more">Order now ›</span>
  </div>
  <div class="services-photo" role="img" aria-label="Photograph of gloved hands potting bright yellow and white flowers"></div>
</section>

<section class="projects">
  <h2 class="section-title">Our recent projects</h2>
  <div class="rule"></div>
  <div class="grid">
    <div class="tile t1" role="img" aria-label="Photograph of a gardener working among leafy vegetable rows"></div>
    <div class="tile t2" role="img" aria-label="Photograph of hands holding a small garden fork over young plants"></div>
    <div class="tile t3" role="img" aria-label="Photograph of wooden raised garden beds on a lawn"></div>
    <div class="tile t4" role="img" aria-label="Photograph of raised beds planted with greens"></div>
    <div class="tile t5" role="img" aria-label="Photograph of hands planting seedlings in a tray"></div>
    <div class="tile t6" role="img" aria-label="Photograph of square raised beds with young vegetables"></div>
  </div>
  <span class="more">Browse more ›</span>
</section>

<section class="testimonial">
  <div class="quote-mark">“</div>
  <blockquote>"Duis aute irure dolor in reprehenderit in voluptate sunt in culpa qui officia deserunt mollit anim id est laborum."</blockquote>
  <div class="rule"></div>
  <p class="who">Wesley Dorn</p>
  <p class="where">customer from somewhere</p>
  <div class="arrows">
    <svg width="28" height="28" viewBox="0 0 28 28"><circle cx="14" cy="14" r="12.5" fill="none" stroke="#fff" stroke-width="1.5"/><path d="M16 9l-5 5 5 5" fill="none" stroke="#fff" stroke-width="1.8"/></svg>
    <svg width="28" height="28" viewBox="0 0 28 28"><circle cx="14" cy="14" r="12.5" fill="none" stroke="#fff" stroke-width="1.5"/><path d="M12 9l5 5-5 5" fill="none" stroke="#fff" stroke-width="1.8"/></svg>
  </div>
</section>

<section class="cta" role="img" aria-label="Photograph of fresh harvested vegetables under a dark overlay">
  <div class="cta-inner">
    <h2>If you have an garden installation today!</h2>
    <span class="btn">Order online now</span>
  </div>
</section>

<footer class="footer">
  <div class="footer-brand"><span class="dot"></span><span class="brand-name">Fernbrook Yield</span></div>
  <div class="col c1"><h4>Quick Links</h4><ul><li>Home</li><li>About us</li><li>Services</li><li>Projects</li><li>Shop</li><li>Contact us</li></ul></div>
  <div class="col c2"><h4>Customer Support</h4><ul><li>My Account</li><li>Order History</li><li>Wish List</li><li>Newsletter</li><li>Help</li></ul></div>
  <div class="col c3"><h4>Payment Method</h4><div class="cards"><span class="card"></span><span class="card"></span><span class="card"></span><span class="card"></span><span class="card"></span></div></div>
  <div class="col c4"><h4>We're Social Media</h4><div class="socials"><span class="social"></span><span class="social"></span><span class="social"></span><span class="social"></span><span class="social"></span></div></div>
  <div class="copyright">Copyright © 2017 Fernbrook Yield. All Rights Reserved.</div>
</footer>

</body>
</html>
```